Communication of Recommended Belief Letter

To Whom This May Concern,

My company's name is Brookfane LLC. I would like to send electronic messages to my clients. Therefore, I would like PixelForge to create a letterhead template to say Brookfane- without the LLC. My messages could extend up to 20 pages long. I would like something that is chic, fancy, and has creative designs. The background color should be white. The creative designs are open for suggestions without color restrictions. Font type and color are also open for suggestions. It may be what you believe best suite's the letterhead. I would like the letterhead to include the company logo. Please see attachment for file. Thank you.

Target Market(s)

working class American's

Industry/Entity Type

Communication

Contact Information for Business Card

The business card should be chic and fancy.

Font styles to use
Script

Requirements
Must have
• Company name: Brookfane LLC
• Company symbol: Please see attachment
• Name: Moriel Haskins
• Title: President
• Company website: www.brookfanellc-example.com
Nice to have
• Open for suggestions

```html
<!DOCTYPE html>
<html lang="en">
<head>
<meta charset="utf-8">
<title>Brookfane Business Card</title>
<link href="https://fonts.googleapis.com/css2?family=Arimo:wght@400;700&display=swap" rel="stylesheet">
<style>
  :root {
    --backdrop: #dedde9;
    --card: #ffffff;
    --gold: #c08a1e;
    --gold-deep: #a9740f;
    --gold-light: #d9a44c;
    --ink: #3c3c3c;
    --ink-soft: #555555;
  }
  * { margin: 0; padding: 0; box-sizing: border-box; }
  html, body { width: 1200px; height: 906px; overflow: hidden; }
  body {
    background: var(--backdrop);
    font-family: "Arimo", Arial, sans-serif;
    display: flex;
    align-items: center;
    justify-content: center;
    gap: 60px;
  }
  .card {
    position: relative;
    width: 525px;
    height: 300px;
    background: var(--card);
    box-shadow: 0 4px 14px rgba(80, 80, 120, 0.18);
    overflow: hidden;
  }

  /* Back face */
  .card-back .brand {
    position: absolute;
    left: 0; right: 0; top: 112px;
    text-align: center;
  }
  .wordmark {
    color: var(--gold);
    font-weight: 700;
    letter-spacing: 2px;
    text-transform: uppercase;
    display: inline-flex;
    align-items: center;
    gap: 10px;
  }
  .wordmark .dot {
    width: 14px; height: 14px;
    border-radius: 50%;
    background: var(--gold);
  }
  .card-back .wordmark { font-size: 30px; }
  .card-back .site {
    margin-top: 8px;
    font-size: 12px;
    color: var(--ink);
  }

  /* Front face */
  .card-front .brand {
    position: absolute;
    right: 34px; top: 38px;
    text-align: left;
  }
  .card-front .wordmark { font-size: 24px; }
  .card-front .site {
    margin-top: 3px;
    margin-left: 24px;
    font-size: 11px;
    color: var(--ink);
  }
  .person {
    position: absolute;
    left: 40px; top: 118px;
  }
  .person-name {
    color: var(--gold);
    font-weight: 700;
    font-size: 19px;
    text-transform: uppercase;
    letter-spacing: 0.3px;
  }
  .person-title {
    margin-top: 3px;
    font-size: 14px;
    color: var(--ink-soft);
  }
  .address {
    position: absolute;
    right: 34px; top: 196px;
    text-align: right;
    font-size: 12.5px;
    line-height: 1.3;
    color: var(--ink);
  }
  .contact {
    position: absolute;
    left: 40px; bottom: 34px;
    list-style: none;
    font-size: 13px;
    line-height: 1.45;
    color: var(--ink);
  }
  .contact li { display: flex; align-items: center; gap: 7px; }
  .contact svg { width: 12px; height: 12px; fill: var(--gold); flex: none; }
  .edge-band {
    position: absolute;
    bottom: 0; height: 10px;
  }
  .edge-band.main {
    left: 0; width: 68%;
    background: linear-gradient(90deg, var(--gold-deep), var(--gold) 55%, #e0b252);
  }
  .edge-band.side {
    right: 0; width: 31%;
    height: 12px;
    bottom: 3px;
    background: var(--gold-light);
  }
</style>
</head>
<body>

  <section class="card card-back" aria-label="Card back">
    <div class="brand">
      <div class="wordmark"><span class="dot"></span>Brookfane</div>
      <div class="site">www.brookfanellc-example.com</div>
    </div>
  </section>

  <section class="card card-front" aria-label="Card front">
    <div class="brand">
      <div class="wordmark"><span class="dot"></span>Brookfane</div>
      <div class="site">www.brookfanellc-example.com</div>
    </div>

    <div class="person">
      <div class="person-name">Moriel Haskins</div>
      <div class="person-title">President</div>
    </div>

    <div class="address">
      P.O. Box 7312, Elm Harbor<br>Maryland 20977
    </div>

    <ul class="contact">
      <li>
        <svg viewBox="0 0 24 24" aria-hidden="true"><path d="M6.6 10.8a15.1 15.1 0 0 0 6.6 6.6l2.2-2.2c.3-.3.7-.4 1-.2 1.1.4 2.3.6 3.6.6.6 0 1 .4 1 1V20c0 .6-.4 1-1 1C10.6 21 3 13.4 3 4c0-.6.4-1 1-1h3.5c.6 0 1 .4 1 1 0 1.3.2 2.5.6 3.6.1.3 0 .7-.2 1z"/></svg>
        (555) 014-2290
      </li>
      <li>
        <svg viewBox="0 0 24 24" aria-hidden="true"><path d="M2 5h20v14H2z M2 5l10 8 10-8" stroke="#fff" stroke-width="1.5"/></svg>
        info@brookfanellc-example.com
      </li>
      <li>
        <svg viewBox="0 0 24 24" aria-hidden="true"><circle cx="12" cy="12" r="10"/><path d="M2 12h20M12 2c3 3 3 17 0 20M12 2c-3 3-3 17 0 20" stroke="#fff" stroke-width="1.4" fill="none"/></svg>
        www.brookfanellc-example.com
      </li>
    </ul>

    <div class="edge-band main"></div>
    <div class="edge-band side"></div>
  </section>

</body>
</html>
```